Flyer Design

We need a flyer design for a small business in Belrose NSW called "Your Vitality Loft". We are a personal training studio. Our service includes: one on one consultation, assessment, a personalised program, personal training.We would like to include the colours as seen in the logo.The flyer design should communicate personalised care in health and fitness.

Target Market(s)

30-80 years, male and female

Industry/Entity Type

Business

Font styles to use
Sans Serif

Requirements
Must have
• Motivating image. Motivating words.

```html
<!DOCTYPE html>
<html lang="en">
<head>
<meta charset="utf-8">
<title>Your Vitality Loft – Flyer</title>
<link href="https://fonts.googleapis.com/css2?family=Lato:wght@400;700;900&family=Oswald:wght@600;700&display=swap" rel="stylesheet">
<style>
  :root {
    --green-dark: #3d5f27;
    --green-mid: #4f7a2f;
    --green-light: #7aa63e;
    --text: #1d1d1b;
    --paper: #ffffff;
    --bg: #e9e9e6;
  }
  * { box-sizing: border-box; margin: 0; padding: 0; }
  html, body { width: 900px; height: 1200px; overflow: hidden; }
  body { background: var(--bg); font-family: 'Lato', sans-serif; color: var(--text); position: relative; }

  .flyer { position: absolute; background: var(--paper); overflow: hidden; box-shadow: 0 4px 14px rgba(0,0,0,.18); }
  .flyer--front { left: 128px; top: 122px; width: 644px; height: 456px; }
  .flyer--back  { left: 128px; top: 668px; width: 647px; height: 464px; }

  .brand { position: absolute; display: flex; align-items: center; gap: 10px; }
  .brand__dot { width: 34px; height: 34px; border-radius: 50%; background: var(--green-mid); }
  .brand__name { font-family: 'Lato', sans-serif; font-weight: 700; font-size: 21px; color: var(--green-mid); }

  .title--front { position: absolute; left: 19px; top: 82px; font-family: 'Oswald', sans-serif; font-weight: 700; font-size: 38px; color: var(--green-dark); letter-spacing: .2px; }
  .title--back  { position: absolute; left: 25px; top: 88px; font-weight: 900; font-size: 21px; color: var(--green-dark); }

  .copy { position: absolute; z-index: 2; font-size: 13px; line-height: 1.3; text-align: justify; }
  .copy p + p { margin-top: 6px; }

  .services { position: absolute; left: 19px; top: 242px; }
  .services h2 { font-size: 20px; font-weight: 700; color: var(--green-dark); margin-bottom: 8px; }
  .services ul { list-style: none; display: grid; grid-template-columns: 180px 170px; row-gap: 5px; }
  .services li { font-size: 14px; font-weight: 700; padding-left: 10px; position: relative; }
  .services li::before { content: ""; position: absolute; left: 0; top: 6px; width: 6px; height: 6px; border-radius: 50%; background: var(--green-mid); }

  .wave { position: absolute; left: 0; bottom: 0; }

  .contacts { position: absolute; z-index: 2; list-style: none; color: #fff; font-size: 12.5px; line-height: 1.38; }
  .contacts li { display: flex; align-items: center; gap: 6px; }
  .contacts svg { width: 10px; height: 10px; flex: none; }

  .photo { position: absolute; }
  .photo--food { left: 375px; top: 6px; width: 268px; height: 232px; border-radius: 70px 0 0 70px; background: linear-gradient(135deg, #8a6a45, #c79a5b 55%, #5c6d3a); }
  .photo--gym { left: 378px; top: 246px; width: 266px; height: 210px; border-radius: 60px 0 0 0; background: linear-gradient(135deg, #3a3f3c, #7b6a5a 60%, #1f2a2e); }
  .photo--treadmill { left: 292px; top: 0; width: 185px; height: 222px; border-radius: 0 0 80px 30px; border: 3px solid var(--green-light); background: linear-gradient(160deg, #d8d9db, #9fa3a8 60%, #cfd3d6); }
  .photo--stretch { left: 478px; top: 0; width: 169px; height: 250px; border-radius: 0 0 0 90px; background: linear-gradient(160deg, #f0ede8, #cdb8a5 55%, #5b7fb6); }
  .photo--athletes { left: 462px; top: 256px; width: 185px; height: 208px; border-radius: 90px 0 0 0; background: linear-gradient(180deg, #f4f4f4, #d9d9d9 55%, #7c7c7c); }
</style>
</head>
<body>

<article class="flyer flyer--front">
  <div class="brand" style="left:22px;top:26px;">
    <span class="brand__dot"></span>
    <span class="brand__name">Your Vitality Loft</span>
  </div>
  <h1 class="title--front">YOUR VITALITY LOFT</h1>
  <div class="copy" style="left:19px;top:138px;width:322px;">
    <p>Your Vitality Loft is a professional exercise clinic which was established at Kellerton in 2005, to service the fitness and health needs of the community.</p>
    <p>The studio has an approach to exercise, which has health at the centre of all physical training programs.</p>
  </div>
  <section class="services">
    <h2>Services</h2>
    <ul>
      <li>one on one consultation</li>
      <li>personalised program</li>
      <li>assessment</li>
      <li>personal training</li>
    </ul>
  </section>

  <div class="photo photo--food" role="img" aria-label="Dumbbell, fresh vegetables, tape measure and water bottle on a wooden table"></div>
  <div class="photo photo--gym" role="img" aria-label="Man training on a cable machine in a gym"></div>

  <svg class="wave" width="644" height="140" viewBox="0 0 644 140" aria-hidden="true">
    <path d="M0 22 C120 -6 260 8 360 60 C420 92 460 126 520 140 L0 140 Z" fill="var(--green-light)"/>
    <path d="M0 34 C120 8 250 20 350 70 C410 100 450 130 500 140 L0 140 Z" fill="var(--green-dark)"/>
  </svg>
  <ul class="contacts" style="left:38px;top:348px;">
    <li><svg viewBox="0 0 10 10"><rect width="10" height="10" rx="2" fill="#1d2a14"/><path d="M3 2.5l1 1.5-1 1 2 2 1-1 1.5 1-1 1.5C4 8 2 6 2 3.5z" fill="#fff"/></svg>(02) 9000 4182</li>
    <li><svg viewBox="0 0 10 10"><rect width="10" height="10" rx="2" fill="#1d2a14"/><path d="M3 2.5l1 1.5-1 1 2 2 1-1 1.5 1-1 1.5C4 8 2 6 2 3.5z" fill="#fff"/></svg>0400 118 265 (DANIEL)</li>
    <li><svg viewBox="0 0 10 10"><rect width="10" height="10" rx="2" fill="#1d2a14"/><path d="M3 2.5l1 1.5-1 1 2 2 1-1 1.5 1-1 1.5C4 8 2 6 2 3.5z" fill="#fff"/></svg>0400 772 309 (MARIA)</li>
    <li><svg viewBox="0 0 10 10"><rect y="2" width="10" height="6" fill="#1d2a14"/><path d="M0 2l5 3 5-3" stroke="#fff" fill="none"/></svg>daniel@yourvitalityloft.com.au</li>
    <li><svg viewBox="0 0 10 10"><circle cx="5" cy="5" r="4.5" fill="#1d2a14"/><path d="M1 5h8M5 .5v9" stroke="#fff" stroke-width=".8"/></svg>www.yourvitalityloft.com.au</li>
  </ul>
</article>

<article class="flyer flyer--back">
  <div class="brand" style="left:22px;top:28px;">
    <span class="brand__dot"></span>
    <span class="brand__name">Your Vitality Loft</span>
  </div>
  <h2 class="title--back">YOUR VITALITY LOFT</h2>
  <div class="copy" style="left:25px;top:124px;width:232px;font-size:12.5px;">
    <p>looks after individuals of all ages and all levels of health and fitness. The Studio is experienced at designing lifestyle plans for people who are starting from a very low level of health and fitness, or who have challenging health issues.</p>
  </div>
  <div class="copy" style="left:25px;top:240px;width:420px;font-size:13.5px;">
    <p>Maria Delane is an exercise specialist at the studio, with expertise in weight management and in coaching individuals towards life-long lifestyle change. When the challenge ahead is arduous, it is important to have the right person working with you along the way.</p>
  </div>

  <div class="photo photo--athletes" role="img" aria-label="Faded silhouettes of a man with an exercise ball and a woman standing in athletic poses"></div>
  <div class="photo photo--treadmill" role="img" aria-label="Woman running on a treadmill"></div>
  <div class="photo photo--stretch" role="img" aria-label="Mature woman stretching on an exercise mat"></div>

  <svg class="wave" width="647" height="120" viewBox="0 0 647 120" aria-hidden="true">
    <path d="M0 10 C130 -8 260 10 340 55 C380 80 410 110 450 120 L0 120 Z" fill="var(--green-light)"/>
    <path d="M0 22 C130 4 250 22 330 65 C370 88 395 112 430 120 L0 120 Z" fill="var(--green-dark)"/>
  </svg>
  <ul class="contacts" style="left:40px;top:364px;">
    <li><svg viewBox="0 0 10 10"><rect width="10" height="10" rx="2" fill="#1d2a14"/><path d="M3 2.5l1 1.5-1 1 2 2 1-1 1.5 1-1 1.5C4 8 2 6 2 3.5z" fill="#fff"/></svg>(02) 9000 4182</li>
    <li><svg viewBox="0 0 10 10"><rect width="10" height="10" rx="2" fill="#1d2a14"/><path d="M3 2.5l1 1.5-1 1 2 2 1-1 1.5 1-1 1.5C4 8 2 6 2 3.5z" fill="#fff"/></svg>0400 118 265 (DANIEL)</li>
    <li><svg viewBox="0 0 10 10"><rect width="10" height="10" rx="2" fill="#1d2a14"/><path d="M3 2.5l1 1.5-1 1 2 2 1-1 1.5 1-1 1.5C4 8 2 6 2 3.5z" fill="#fff"/></svg>0400 772 309 (MARIA)</li>
    <li><svg viewBox="0 0 10 10"><rect y="2" width="10" height="6" fill="#1d2a14"/><path d="M0 2l5 3 5-3" stroke="#fff" fill="none"/></svg>daniel@yourvitalityloft.com.au</li>
    <li><svg viewBox="0 0 10 10"><circle cx="5" cy="5" r="4.5" fill="#1d2a14"/><path d="M1 5h8M5 .5v9" stroke="#fff" stroke-width=".8"/></svg>www.yourvitalityloft.com.au</li>
  </ul>
</article>

</body>
</html>
```